Coastal waterside shopping complex needs a billboard sign

"Harbour Verge" is the name of a building which comprises 4 shops in a coastal waterside location. We need a 2440mm (Wide) x 1100mm (High) "Harbour Verge" billboard design that will fit with the coastal theme but is modern and contemporary, positioning the building as a high class mini shopping complex.

The photo below is for reference only. We only need a design for the "Harbour Verge" sign.

The end product will need to be an EPS scalable vector file.

```html
<!DOCTYPE html>
<html lang="en">
<head>
<meta charset="utf-8">
<title>Harbour Verge Billboard</title>
<link href="https://fonts.googleapis.com/css2?family=Montserrat:wght@700&display=swap" rel="stylesheet">
<style>
  :root {
    --backdrop: #8c8c8c;
    --sign-teal: #04716a;
    --sign-ink: #ffffff;
  }
  html, body {
    margin: 0;
    padding: 0;
    width: 1200px;
    height: 1200px;
    overflow: hidden;
    background: var(--backdrop);
  }
  .canvas {
    position: relative;
    width: 1200px;
    height: 1200px;
  }
  .billboard {
    position: absolute;
    left: 60px;
    top: 356px;
    width: 1080px;
    height: 487px;
    box-sizing: border-box;
    background: var(--sign-teal);
    box-shadow: 0 3px 6px rgba(0, 0, 0, 0.25);
    display: flex;
    align-items: center;
    justify-content: center;
  }
  .billboard__name {
    margin: 0;
    color: var(--sign-ink);
    font-family: "Montserrat", Arial, sans-serif;
    font-weight: 700;
    font-size: 140px;
    line-height: 1.08;
    letter-spacing: 0.02em;
    text-align: center;
    text-transform: uppercase;
  }
</style>
</head>
<body>
  <main class="canvas">
    <section class="billboard" aria-label="Harbour Verge billboard sign">
      <h1 class="billboard__name">Harbour<br>Verge</h1>
    </section>
  </main>
</body>
</html>
```